Tidewell Ventures Wordpress / Web Design - Agile Coaching

UPDATE: PLEASE USE MORE ICONS/GRAPHICS THEN PHOTOS. THANK YOU!

We need a web design for a new company called Tidewell Ventures. We do agile coaching, consulting, training and facilitation for medium to large enterprise, most just starting their agile journey. We want to be professional, but light and whimsical. We have started loading content onto the www.tidewellventures.example website, using the Marlow Theme (real flexibility!)

We have a logo, and I really liked it, although if needed the colors can be adjusted depending on the design. I would advice sticking with the logo and its colors unless they become problematic or you have a fantastic idea.

I really like the colors found on stickum slips, and use stickum slips in all my coaching and training. I want to warn though, I don't want the whole site to be splashes of color, but I would like some pop of color, and you could use the stickum slip colors and the idea of stickum slips for icon designs or sparingly for emphasis, but keep the design simple with lots of white space. I'm inspired by this template from Pattern Bazaar and use the power point in the 2nd attached file...this may inspire you.

I have another contest running right now, if you want to check that out as well, but it isn't necessary. Contest is titled "Tidewell Ventures: Software Development Consultancy Needs a Business Card Design"

Target Market(s)

medium to large software companies needing to improve the speed, quality and value of their software delivery

Industry/Entity Type

Information Technology

Number of Pages Required

3 page

Font styles to use
Sans Serif

Requirements
Must have
• Simple, easy to use, easy navigation, space!
• content on my front page is accurate so should be included www.tidewellventures.example
• 2nd page you can look at is http://www.tidewellventures.example/inspiration/
• 3rd page you can look at is http://www.tidewellventures.example/reference-list/ (about twice as many links are going to be added in next two days!)
Nice to have
• take a look at any other page on the site. if something is password protected, use the word "password" as the password.
• Update: I like less pictures, more graphics.
Should not have
• too crowded. hard to navigate. childish graphics. too boring and corporate. :)

```html
<!DOCTYPE html>
<html lang="en">
<head>
<meta charset="utf-8">
<title>Tidewell Ventures</title>
<link href="https://fonts.googleapis.com/css2?family=Open+Sans:wght@400;600;700&display=swap" rel="stylesheet">
<style>
:root{
  --brand:#1f6f9e;
  --ink:#333a40;
  --muted:#7b8288;
  --line:#e3e6e9;
  --hero-blue:#2b86c5;
  --hero-red:#d8343a;
  --red:#e04a3f;
  --purple:#8e4c93;
  --green:#8cc63f;
  --blue:#2c8fd6;
  --band:#86497f;
  --feed-bg:#eef0f2;
  --feed-a:#2f5fa8;
  --feed-b:#38a9e6;
}
*{box-sizing:border-box;margin:0;padding:0}
html,body{width:802px;height:1200px;overflow:hidden;background:#fff}
body{font-family:"Open Sans",Arial,sans-serif;color:var(--ink);position:relative}
.wrap{width:544px;margin:0 auto}

/* header */
.site-header{height:70px;display:flex;align-items:center;justify-content:space-between;padding:0 128px}
.brand{display:flex;align-items:center;gap:8px}
.brand-dot{width:26px;height:26px;border-radius:50%;background:var(--brand)}
.brand-name{font-size:15px;font-weight:700;color:var(--brand);line-height:1}
.main-nav{display:flex;gap:14px;align-items:center;font-size:8px;font-weight:600;letter-spacing:.4px}
.main-nav a{color:var(--ink);text-decoration:none}
.phone{display:flex;align-items:center;gap:4px;color:var(--ink)}

/* hero */
.hero{width:660px;height:302px;margin:0 auto;position:relative;overflow:hidden;
  background:linear-gradient(100deg,#f3f4f5 0%,#e9ebec 45%,#d9d6d2 70%,#c9c2bb 100%)}
.hero-photo{position:absolute;right:0;top:0;width:62%;height:100%;
  background:radial-gradient(ellipse at 55% 60%,#b9aea4 0%,#d4ccc4 40%,rgba(233,235,236,0) 75%)}
.hero-copy{position:absolute;left:55px;top:168px;width:340px}
.hero-title{font-size:19px;font-weight:400;color:var(--hero-blue);line-height:1.2;white-space:nowrap}
.hero-sub{font-size:17px;color:var(--hero-red);line-height:1.3;margin-bottom:8px;white-space:nowrap}
.hero-text{font-size:7px;color:var(--muted);line-height:1.5;width:210px;margin-bottom:8px}
.btn{display:inline-block;font-size:6.5px;font-weight:700;letter-spacing:.4px;color:#fff;padding:4px 10px;border-radius:2px;text-transform:uppercase}
.btn-red{background:var(--hero-red)}
.slider-dots{position:absolute;bottom:10px;left:50%;transform:translateX(-50%);display:flex;gap:5px}
.slider-dots span{width:6px;height:6px;border-radius:50%;background:#fff;opacity:.7}
.slider-dots span.on{opacity:1;box-shadow:0 0 0 1px #ccc}

/* intro & services */
.intro{height:305px;text-align:center;padding-top:48px}
.intro h1{font-size:19px;font-weight:400;color:var(--ink);margin-bottom:6px}
.intro h2{font-size:12px;font-weight:400;color:var(--brand);margin-bottom:32px}
.services{display:flex;justify-content:space-between;align-items:flex-start}
.service{width:130px;text-align:center}
.service svg{width:40px;height:40px;display:block;margin:0 auto 8px}
.service h3{font-size:9.5px;font-weight:600;margin-bottom:5px}
.service p{font-size:6.5px;color:var(--muted);line-height:1.5;margin:0 8px 8px;height:30px}
.service .btn{font-size:5.5px;padding:3px 9px}
.c-red{color:var(--red)}.c-purple{color:var(--purple)}.c-green{color:var(--green)}.c-blue{color:var(--blue)}
.bg-red{background:var(--red)}.bg-purple{background:var(--purple)}.bg-green{background:var(--green)}.bg-blue{background:var(--blue)}

/* blogs */
.blogs{height:245px;background:var(--band);padding-top:36px}
.blogs h2{font-size:14px;font-weight:600;color:#fff;margin-bottom:10px}
.blog-list{display:flex;justify-content:space-between}
.post{width:176px;color:#fff}
.post-photo{height:76px;margin-bottom:6px;background:linear-gradient(135deg,#c9b6a4,#8d7466 60%,#5f4e48)}
.post:nth-child(2) .post-photo{background:linear-gradient(135deg,#d9d2c8,#a2948a 55%,#6e625c)}
.post:nth-child(3) .post-photo{background:linear-gradient(135deg,#b7a59a,#8a6d62 50%,#5a4744)}
.post h3{font-size:8.5px;font-weight:600;margin-bottom:3px}
.post p{font-size:6px;line-height:1.5;opacity:.85;margin-bottom:6px}
.post a{font-size:6px;color:#fff;text-decoration:none;font-weight:600}

/* feeds */
.feeds{height:215px;background:var(--feed-bg);padding-top:34px}
.feed-list{display:flex;justify-content:space-between;align-items:flex-start}
.feed{width:262px;background:#fff}
.feed-head{height:18px;font-size:8px;font-weight:600;color:#fff;padding:4px 8px}
.feed-a .feed-head{background:var(--feed-a)}
.feed-b .feed-head{background:var(--feed-b)}
.entry{display:flex;gap:7px;padding:12px 10px;border-bottom:1px solid var(--line)}
.entry:last-child{border-bottom:0;padding-bottom:16px}
.avatar{width:20px;height:20px;border-radius:50%;background:linear-gradient(135deg,#b9c2ca,#8c96a0);flex:none}
.entry strong{display:block;font-size:6.5px;font-weight:600;margin-bottom:2px}
.entry p{font-size:6px;color:var(--muted);line-height:1.5}

/* footer */
.site-footer{height:63px;padding:14px 128px 0;position:relative}
.foot-nav{display:flex;gap:14px;font-size:7px;font-weight:600;margin-bottom:6px}
.foot-nav a{color:var(--ink);text-decoration:none}
.copy{font-size:5.5px;color:var(--muted)}
.social{position:absolute;right:128px;top:16px;display:flex;gap:6px}
.social span{width:7px;height:7px;background:var(--blue)}
</style>
</head>
<body>

<header class="site-header">
  <div class="brand"><span class="brand-dot"></span><span class="brand-name">Tidewell Ventures</span></div>
  <nav class="main-nav">
    <a href="#">ABOUT</a><a href="#">INSPIRATION</a><a href="#">BLOG</a><a href="#">SERVICES</a><a href="#">CONTACT</a>
    <span class="phone">
      <svg width="8" height="8" viewBox="0 0 24 24"><path fill="#2c8fd6" d="M6.6 10.8a15 15 0 006.6 6.6l2.2-2.2a1 1 0 011-.25 11.4 11.4 0 003.6.57 1 1 0 011 1V20a1 1 0 01-1 1A17 17 0 013 4a1 1 0 011-1h3.5a1 1 0 011 1 11.4 11.4 0 00.57 3.6 1 1 0 01-.25 1z"/></svg>
      (555) 014-2290
    </span>
  </nav>
</header>

<section class="hero">
  <div class="hero-photo" role="img" aria-label="Photo of a trainer coaching a woman doing push-ups on a balance ball in a bright studio"></div>
  <div class="hero-copy">
    <p class="hero-title">Cum sociis natoque penatibus</p>
    <p class="hero-sub">Mauris vel lacus vitae felis</p>
    <p class="hero-text">Sed ut perspiciatis unde omnis iste natus error sit voluptatem accusantium doloremque laudantium totam rem.</p>
    <span class="btn btn-red">Learn more</span>
  </div>
  <div class="slider-dots"><span class="on"></span><span></span><span></span></div>
</section>

<section class="intro">
  <div class="wrap">
    <h1>Lorem ipsum dolor sit amet consectetuer adipiscing</h1>
    <h2>Mauris vel lacus vitae felis vestibulum volutpat</h2>
    <div class="services">
      <div class="service">
        <svg viewBox="0 0 40 40"><path d="M6 8h20a3 3 0 013 3v10a3 3 0 01-3 3H14l-6 5v-5H6a3 3 0 01-3-3V11a3 3 0 013-3z" fill="none" stroke="#e04a3f" stroke-width="2"/><path d="M31 14h3a3 3 0 013 3v9a3 3 0 01-3 3h-1v4l-5-4h-8" fill="none" stroke="#e04a3f" stroke-width="2"/></svg>
        <h3 class="c-red">Agile Consulting</h3>
        <p>Nam liber tempor cum soluta nobis eleifend option congue nihil.</p>
        <span class="btn bg-red">Read more</span>
      </div>
      <div class="service">
        <svg viewBox="0 0 40 40"><rect x="8" y="6" width="26" height="18" fill="none" stroke="#8e4c93" stroke-width="2"/><path d="M14 24l-4 12M28 24l4 12M21 24v8" stroke="#8e4c93" stroke-width="2"/><circle cx="7" cy="20" r="3" fill="#8e4c93"/><path d="M3 34v-6a4 4 0 018 0v6" fill="#8e4c93"/></svg>
        <h3 class="c-purple">Agile Training</h3>
        <p>Typi non habent claritatem insitam est usus legentis in iis.</p>
        <span class="btn bg-purple">Read more</span>
      </div>
      <div class="service">
        <svg viewBox="0 0 40 40"><rect x="9" y="7" width="22" height="28" rx="2" fill="none" stroke="#8cc63f" stroke-width="2"/><rect x="15" y="4" width="10" height="6" rx="1" fill="#8cc63f"/><path d="M14 21l4 4 8-9" fill="none" stroke="#8cc63f" stroke-width="2.5"/></svg>
        <h3 class="c-green">Agile Coaching</h3>
        <p>Claritas est etiam processus dynamicus qui sequitur mutationem.</p>
        <span class="btn bg-green">Read more</span>
      </div>
      <div class="service">
        <svg viewBox="0 0 40 40"><rect x="15" y="4" width="10" height="8" fill="#2c8fd6"/><rect x="4" y="28" width="10" height="8" fill="#2c8fd6"/><rect x="26" y="28" width="10" height="8" fill="#2c8fd6"/><path d="M20 12v8M9 28v-8h22v8" fill="none" stroke="#2c8fd6" stroke-width="2"/></svg>
        <h3 class="c-blue">Agile Facilitation</h3>
        <p>Mirum est notare quam littera gothica quam nunc putamus parum.</p>
        <span class="btn bg-blue">Read more</span>
      </div>
    </div>
  </div>
</section>

<section class="blogs">
  <div class="wrap">
    <h2>LATEST BLOGS</h2>
    <div class="blog-list">
      <article class="post">
        <div class="post-photo" role="img" aria-label="Photo of a group fitness class"></div>
        <h3>Cras a ante vitae enim</h3>
        <p>Aliquam erat volutpat ut wisi enim ad minim veniam quis nostrud exerci tation ullamcorper suscipit lobortis nisl.</p>
        <a href="#">Read more</a>
      </article>
      <article class="post">
        <div class="post-photo" role="img" aria-label="Photo of a coach working with a client"></div>
        <h3>Proin nulla arcu consectetur</h3>
        <p>Ut wisi enim ad minim veniam quis nostrud exerci tation ullamcorper suscipit lobortis nisl ut aliquip ex commodo.</p>
        <a href="#">Read more</a>
      </article>
      <article class="post">
        <div class="post-photo" role="img" aria-label="Photo of a training session in a gym"></div>
        <h3>Etiam eu urna sed porta</h3>
        <p>Duis autem vel eum iriure dolor in hendrerit in vulputate velit esse molestie consequat vel illum dolore eu.</p>
        <a href="#">Read more</a>
      </article>
    </div>
  </div>
</section>

<section class="feeds">
  <div class="wrap feed-list">
    <div class="feed feed-a">
      <div class="feed-head">Community Feed</div>
      <div class="entry"><span class="avatar"></span><div><strong>Dana Whitfield @danawhit</strong><p>Duis autem vel eum iriure dolor in hendrerit.</p></div></div>
      <div class="entry"><span class="avatar"></span><div><strong>Corin Haldane @corinhal</strong><p>Nam liber tempor cum soluta nobis eleifend.</p></div></div>
    </div>
    <div class="feed feed-b">
      <div class="feed-head">Updates Feed</div>
      <div class="entry"><span class="avatar"></span><div><strong>Dana Whitfield @danawhit</strong><p>Typi non habent claritatem insitam est usus.</p></div></div>
      <div class="entry"><span class="avatar"></span><div><strong>Corin Haldane @corinhal</strong><p>Mirum est notare quam littera gothica nunc.</p></div></div>
    </div>
  </div>
</section>

<footer class="site-footer">
  <nav class="foot-nav"><a href="#">HOME</a><a href="#">ABOUT</a><a href="#">SERVICES</a><a href="#">BLOG</a><a href="#">INSPIRATION</a><a href="#">CONTACT</a></nav>
  <p class="copy">© 2024 Tidewell Ventures. All rights reserved. Terms of Use</p>
  <div class="social"><span></span><span></span><span></span></div>
</footer>

</body>
</html>
```